Menu Design for Chocolate and Cheese Shop

We are chocolate (and cheese) makers - www.velmarita.com.au and would like to redesign our café menu (attached is the pdf of the old one). I would like to end up with a file using Adobe suite of products so we can readily update menus as we change them. Clean, classy and inviting. We would also like to incorporate our cheese with our sister business into the menu offering (www.dunhollowmead.com.au and www.facebook.com/dunhollowmead). Just allow space for us to flesh out content for the cheese menu items - we will definitely include our Tall Platter in this if you see our facebook posts) - 4pp - A4 landscape folded into A5. We would also like the exact same menu but with our Dunhollow Mead Branding instead of velmarita (we have two different sites -attached are our dunhollow mead logos as well for incorporating into the second document)

```html
<!DOCTYPE html>
<html lang="en">
<head>
<meta charset="utf-8">
<title>Velmarita Café Menu – Sweet Treats &amp; Drinks</title>
<link href="https://fonts.googleapis.com/css2?family=Alegreya+Sans+SC:wght@700;800&family=Josefin+Sans:wght@400;600;700&family=Lato:ital,wght@0,400;0,700;1,700&display=swap" rel="stylesheet">
<style>
:root{
  --taupe:#857568;
  --night:#2f2725;
  --header:#2c2523;
  --cocoa:#3d3330;
  --ink:#2a2421;
  --body:#3b3431;
  --paper:#ffffff;
  --muted:#9a8f88;
  --band:#151212;
}
*{box-sizing:border-box;margin:0;padding:0}
html,body{width:1200px;height:1000px;overflow:hidden}
body{position:relative;background:var(--night);font-family:"Lato",sans-serif;color:var(--body)}
.backdrop-left{position:absolute;left:0;top:0;width:683px;height:1000px;background:var(--taupe)}

.page{position:absolute;background:var(--paper);overflow:hidden}
.title{font-family:"Alegreya Sans SC",sans-serif;font-weight:800;color:var(--ink);letter-spacing:.4px}
.price{position:absolute;right:0;top:0;font-family:"Alegreya Sans SC",sans-serif;font-weight:800;color:var(--ink);white-space:nowrap}
.item{position:absolute}
.desc{font-size:10.5px;line-height:12.6px;color:var(--body)}
.desc b{font-weight:700;font-style:italic;color:var(--ink)}

.section-head{position:absolute;left:0;right:0;text-align:center;font-family:"Josefin Sans",sans-serif;letter-spacing:4px;line-height:1.15}
.rule{position:absolute;height:2px;background:currentColor}
.dot{position:absolute;width:8px;height:8px;border-radius:50%;background:currentColor}

/* Back sweet treats page */
.back-treats{left:16px;top:18px;width:557px;height:787px}
.back-treats .head{position:absolute;left:0;top:0;width:100%;height:124px;background:var(--header);color:#fff}
.back-treats .brand{position:absolute;left:0;right:0;top:30px;text-align:center;font-family:"Alegreya Sans SC",sans-serif;font-weight:800;font-size:14px;letter-spacing:.6px}
.back-treats .brand i{display:inline-block;width:9px;height:9px;border-radius:50%;background:#fff;margin-right:6px;vertical-align:1px}
.back-treats .section-head{top:70px;font-size:17px;font-weight:400}
.back-treats .item{left:46px;right:29px}
.back-treats .title{font-size:15px}
.back-treats .price{font-size:15px}
.back-treats .desc{font-size:12px;line-height:14px;margin-top:3px}
.back-treats .kids-band{position:absolute;left:42px;top:637px;background:var(--band);color:#fff;font-family:"Josefin Sans",sans-serif;font-weight:700;font-size:13px;letter-spacing:1.4px;padding:2px 6px 0;white-space:nowrap}

/* Back drinks page */
.back-drinks{left:573px;top:18px;width:557px;height:700px;background:transparent}
.back-drinks .head{position:absolute;left:0;top:0;width:100%;height:92px;background:var(--night);color:#fff}
.back-drinks .section-head{top:22px;font-size:17px;font-weight:400}
.back-drinks .body{position:absolute;left:0;top:92px;width:100%;bottom:0;background:var(--paper)}
.back-drinks .item{left:40px;right:37px}
.back-drinks .title{font-size:15px}
.back-drinks .desc{font-size:12px;line-height:14px;margin-top:2px;max-width:370px}
.back-drinks .sizes{position:absolute;right:0;top:0;font-family:"Alegreya Sans SC",sans-serif;font-weight:800;font-size:15px;line-height:23px;color:var(--ink);text-align:right}

/* Front sweet treats page */
.front-treats{left:197px;top:285px;width:492px;height:697px;box-shadow:-2px 0 6px rgba(0,0,0,.12)}
.front-treats .head{position:absolute;left:0;top:0;width:100%;height:53px;background:var(--cocoa)}
.front-treats .url{position:absolute;left:25px;top:16px;font-size:9px;color:var(--muted);font-style:italic}
.brandmark{position:absolute;font-family:"Lato",sans-serif;font-weight:400;color:#c9bfb6;font-size:15px;letter-spacing:.2px;display:flex;align-items:center;gap:7px}
.brandmark i{display:block;width:14px;height:14px;border-radius:50%;background:#c9bfb6}
.front-treats .brandmark{right:16px;top:17px}
.front-treats .section-head{top:74px;font-size:14.5px;font-weight:400;color:var(--ink)}
.front-treats .item{left:41px;right:29px}
.front-treats .title{font-size:13px}
.front-treats .price{font-size:13px}
.front-treats .desc{margin-top:3px;max-width:330px}
.front-treats .kids-band{position:absolute;left:40px;top:561px;z-index:2;background:var(--cocoa);color:#fff;font-family:"Josefin Sans",sans-serif;font-weight:700;font-size:10.5px;letter-spacing:1px;line-height:15px;padding:1px 5px 0;white-space:nowrap}
.kids-lines{position:absolute;left:165px;right:29px;top:567px;height:6px;border-top:2px solid var(--ink);border-bottom:1px solid var(--ink);z-index:1}
.kid{position:absolute;font-family:"Alegreya Sans SC",sans-serif;font-weight:800;font-size:12.5px;color:var(--ink);display:flex;justify-content:space-between}
.kid.col-a{left:41px;width:206px}
.kid.col-b{left:273px;width:190px}

/* Front drinks page */
.front-drinks{left:689px;top:285px;width:493px;height:697px}
.front-drinks .section-head{top:26px;font-size:14.5px;font-weight:400;color:var(--ink)}
.front-drinks .item{left:35px;right:34px}
.front-drinks .title{font-size:13px}
.front-drinks .price{font-size:13px}
.front-drinks .desc{margin-top:2px;max-width:310px}
.front-drinks .sizes{position:absolute;right:0;top:0;font-family:"Alegreya Sans SC",sans-serif;font-weight:800;font-size:13px;line-height:19.5px;color:var(--ink);text-align:right}
.front-drinks .foot{position:absolute;left:0;bottom:0;width:100%;height:52px;background:var(--cocoa)}
.front-drinks .brandmark{left:0;right:0;justify-content:center;top:18px}

.cup{position:absolute}

.presentation-label{position:absolute;left:20px;top:822px;color:var(--ink);font-family:"Josefin Sans",sans-serif}
.presentation-label .l1{font-size:40px;font-weight:400;letter-spacing:10px;line-height:48px}
.presentation-label .l2{font-size:27px;font-weight:400;letter-spacing:7px;line-height:44px;margin-top:8px}
.presentation-label .l3{font-size:24px;font-weight:700;letter-spacing:2.5px;line-height:40px;margin-top:4px}
</style>
</head>
<body>
<div class="backdrop-left"></div>

<!-- Back: sweet treats, Dunhollow Mead edition -->
<section class="page back-treats">
  <div class="head">
    <div class="brand"><i></i>DUNHOLLOW MEAD</div>
    <div class="rule" style="left:112px;top:89px;width:72px"></div>
    <div class="dot" style="left:203px;top:86px"></div>
    <h2 class="section-head">SWEET<br>TREATS</h2>
    <div class="dot" style="left:343px;top:86px"></div>
    <div class="rule" style="left:372px;top:89px;width:72px"></div>
  </div>
  <div class="item" style="top:145px"><div class="title">Chocolate Taste Plate</div><div class="price">$14.30</div><p class="desc">chocolate macaron, chocolate ice cream,&nbsp; chocolate mousse,<br>and our signature chocolate</p></div>
  <div class="item" style="top:213px"><div class="title">Caramel Taste Plate</div><div class="price">$14.30</div><p class="desc">caramel slice, hokey pokey ice cream, caramel truffle, and<br>alfajores (Spanish shortbread) filled with dulce de leche</p></div>
  <div class="item" style="top:281px"><div class="title">Raspberry Brownie</div><div class="price">$12.50</div><p class="desc">Brownie topped with raspberries, served warm with a scoop of<br>vanilla bean ice cream</p></div>
  <div class="item" style="top:351px"><div class="title">Ice Cream Sensation</div><div class="price">$12.00</div><p class="desc">a trio of chocolate ice cream or our weekly special ice cream<br>served with chocolate sauce and sprinkled with dark crispy<br>pearls (ask our team what flavour is available)</p></div>
  <div class="item" style="top:431px"><div class="title">Chocolate Mousse</div><div class="price">$12.00</div><p class="desc">rich and creamy chocolate mousse served with white crispy pearls</p></div>
  <div class="item" style="top:486px"><div class="title">Handmade Chocolates</div><div class="price">from $1.90</div><p class="desc">choose from our extensive range of fresh chocolates and truffles</p></div>
  <div class="item" style="top:541px"><div class="title">Dessert Jars</div><div class="price">$15.50</div><p class="desc">ask our team to find out what is on offer this week</p></div>
  <div class="item" style="top:597px"><div class="title">Handmade Cookies</div><div class="price">$3.00</div></div>
  <div class="kids-band">FOR THE CHILDREN</div>
  <div class="item" style="top:667px"><div class="title">Mini Hot Chocolate</div></div>
  <div class="item" style="top:693px"><div class="title">Mini Chino</div></div>
  <div class="item" style="top:718px"><div class="title">Mini Chino With Cubby Pop</div></div>
</section>

<!-- Back: drinks, Dunhollow Mead edition -->
<section class="page back-drinks">
  <div class="head">
    <div class="rule" style="left:107px;top:41px;width:72px"></div>
    <div class="dot" style="left:196px;top:38px"></div>
    <h2 class="section-head">DRINKS</h2>
    <div class="dot" style="left:358px;top:38px"></div>
    <div class="rule" style="left:384px;top:41px;width:72px"></div>
    <svg class="cup" style="left:267px;top:49px" width="24" height="22" viewBox="0 0 24 22" fill="none" stroke="#fff" stroke-width="1.4" aria-hidden="true"><path d="M4 8h13v5a5 5 0 0 1-5 5H9a5 5 0 0 1-5-5z"/><path d="M17 10h2a2 2 0 0 1 0 4h-2"/><path d="M2 20h19"/><path d="M8 2c-1 1.5 1 2.5 0 4M12 2c-1 1.5 1 2.5 0 4"/></svg>
  </div>
  <div class="body">
    <div class="item" style="top:14px"><div class="title">Hot Chocolate</div><div class="sizes">Reg ~ $5.50<br>Lrg ~ $6.00</div><p class="desc"><b>traditional</b> - made with 65% maracaibo single origin chocolate<br><b>white</b> - made with white chocolate<br><b>half and half</b> - halt traditional and half white hot chocolate</p></div>
    <div class="item" style="top:93px"><div class="title">Mocha</div><div class="sizes">Reg ~ $6.00<br>Lrg ~ $6.50</div><p class="desc">can be made with traditional or white chocolate</p></div>
    <div class="item" style="top:139px"><div class="title">Special Hot Chocolate</div><div class="sizes">Reg ~ $6.50<br>Lrg ~ $7.00</div><p class="desc">a creamy ganache made with crème fraiche&nbsp; infused with a different flavour each week (ask our team what flavour is available)</p></div>
  </div>
</section>

<!-- Front: sweet treats, Velmarita edition -->
<section class="page front-treats">
  <div class="head">
    <span class="url">www.velmarita.com.au</span>
    <div class="brandmark">velmarita<i></i></div>
  </div>
  <div class="rule" style="left:98px;top:90px;width:65px;color:var(--ink)"></div>
  <div class="dot" style="left:180px;top:87px;color:var(--ink)"></div>
  <h2 class="section-head">SWEET<br>TREATS</h2>
  <div class="dot" style="left:302px;top:87px;color:var(--ink)"></div>
  <div class="rule" style="left:328px;top:90px;width:63px;color:var(--ink)"></div>

  <div class="item" style="top:121px"><div class="title">Chocolate Taste Plate</div><div class="price">$14.30</div><p class="desc">chocolate macaron, chocolate ice cream,&nbsp; chocolate mousse,<br>and our signature chocolate</p></div>
  <div class="item" style="top:181px"><div class="title">Caramel Taste Plate</div><div class="price">$14.30</div><p class="desc">caramel slice, hokey pokey ice cream, caramel truffle, and<br>alfajores (Spanish shortbread) filled with dulce de leche</p></div>
  <div class="item" style="top:242px"><div class="title">Raspberry Brownie</div><div class="price">$12.50</div><p class="desc">Brownie topped with raspberries, served warm with a scoop of<br>vanilla bean ice cream</p></div>
  <div class="item" style="top:303px"><div class="title">Ice Cream Sensation</div><div class="price">$12.00</div><p class="desc">a trio of chocolate ice cream or our weekly special ice cream<br>served with chocolate sauce and sprinkled with dark crispy<br>pearls (ask our team what flavour is available)</p></div>
  <div class="item" style="top:374px"><div class="title">Chocolate Mousse</div><div class="price">$12.00</div><p class="desc">rich and creamy chocolate mousse served with white crispy pearls</p></div>
  <div class="item" style="top:423px"><div class="title">Handmade Chocolates</div><div class="price">from $1.90</div><p class="desc">choose from our extensive range of fresh chocolates and truffles</p></div>
  <div class="item" style="top:471px"><div class="title">Dessert Jars</div><div class="price">$15.50</div><p class="desc">ask our team to find out what is on offer this week</p></div>
  <div class="item" style="top:520px"><div class="title">Handmade Cookies</div><div class="price">$3.00</div></div>

  <div class="kids-band">FOR THE CHILDREN</div>
  <div class="kids-lines"></div>
  <div class="kid col-a" style="top:589px"><span>Mini Hot Chocolate</span><span>$3.00</span></div>
  <div class="kid col-a" style="top:612px"><span>Mini Chino</span><span>$1.00</span></div>
  <div class="kid col-a" style="top:635px"><span>Mini Chino With Cubby Pop</span><span>$2.50</span></div>
  <div class="kid col-b" style="top:589px"><span>Mini Ice Chocolate</span><span>$5.00</span></div>
  <div class="kid col-b" style="top:612px"><span>Mini Ice Cream</span><span>$3.50</span></div>
  <div class="kid col-b" style="top:635px"><span>Mini Mousse</span><span>$3.50</span></div>
</section>

<!-- Front: drinks, Velmarita edition -->
<section class="page front-drinks">
  <div class="rule" style="left:93px;top:43px;width:63px;color:var(--ink)"></div>
  <div class="dot" style="left:170px;top:40px;color:var(--ink)"></div>
  <h2 class="section-head">DRINKS</h2>
  <div class="dot" style="left:315px;top:40px;color:var(--ink)"></div>
  <div class="rule" style="left:338px;top:43px;width:63px;color:var(--ink)"></div>
  <svg class="cup" style="left:236px;top:51px" width="22" height="20" viewBox="0 0 24 22" fill="none" stroke="#2a2421" stroke-width="1.4" aria-hidden="true"><path d="M4 8h13v5a5 5 0 0 1-5 5H9a5 5 0 0 1-5-5z"/><path d="M17 10h2a2 2 0 0 1 0 4h-2"/><path d="M2 20h19"/><path d="M8 2c-1 1.5 1 2.5 0 4M12 2c-1 1.5 1 2.5 0 4"/></svg>

  <div class="item" style="top:77px"><div class="title">Hot Chocholate</div><div class="sizes">Reg ~ $5.50<br>Lrg ~ $6.00</div><p class="desc"><b>traditional</b> - made with 65% maracaibo single origin chocolate<br><b>white</b> - made with white chocolate<br><b>half and half</b> - halt traditional and half white hot chocolate</p></div>
  <div class="item" style="top:147px"><div class="title">Mocha</div><div class="sizes">Reg ~ $6.00<br>Lrg ~ $6.50</div><p class="desc">can be made with traditional or white chocolate</p></div>
  <div class="item" style="top:187px"><div class="title">Special Hot Chocolate</div><div class="sizes">Reg ~ $6.50<br>Lrg ~ $7.00</div><p class="desc">a creamy ganache made with crème fraiche&nbsp; infused with a different flavour each week (ask our team what flavour is available)</p></div>
  <div class="item" style="top:252px"><div class="title">Coffee</div><div class="sizes">Reg ~ $4.00<br>Lrg ~ $4.50</div><p class="desc">latte, cappuccino, flat white, long black, short black, short macchiato, long macchiato, piccolo latte</p></div>
  <div class="item" style="top:306px"><div class="title">Chai</div><div class="price">Reg ~ $4.00 &nbsp;|&nbsp; Lrg ~ $4.50</div></div>
  <div class="item" style="top:335px"><div class="title">Tea - A Pot of Leafwell Organic Tea</div><div class="price">$5.00</div><p class="desc">english breakfast, earlgrey, french earlgrey, wellbeing,<br>coconut, berry green, white tea and rose, chai, dark tea &amp;<br>chocolate, lemongrass and ginger</p></div>
  <div class="item" style="top:403px"><div class="title">Affogato</div><div class="price">$6.00</div><p class="desc">vanilla bean ice cream served with a shot of coffee or<br>molten chocolate</p></div>
  <div class="item" style="top:455px"><div class="title">Iced Coffee</div><div class="price">$5.50</div></div>
  <div class="item" style="top:482px"><div class="title">Iced Chocolate</div><div class="price">$7.00</div><p class="desc">white or 65% maracaibo single origin chocolate with our special<br>blend of hollowell cream, milk, and chocolate</p></div>
  <div class="item" style="top:537px"><div class="title">Iced Mocha - White or Traditional</div><div class="price">$7.50</div></div>
  <div class="item" style="top:565px"><div class="title">Milkshakes</div><div class="price">$6.00</div><p class="desc">chocolate, (our own decadent fudge, vanilla or caramel)</p></div>
  <div class="item" style="top:609px"><div class="title">Kelvale - Still or Sparkling Water</div><div class="price">$3.00</div></div>

  <div class="foot"><div class="brandmark">velmarita<i></i></div></div>
</section>

<div class="presentation-label">
  <div class="l1">MENU</div>
  <div class="l2">DESIGN</div>
  <div class="l3">A4 PAPER</div>
</div>
</body>
</html>
```